Business Card Design Project - 2 sided

We need a business card design for a card having one business on each side (ie. two businesses on one card). Would like a design that incorporates logo, tagline and normal fields (name, position, address, phone).

Would also like an allowance for small font text along the bottom (text to be determined, but less than 50 characters).

NB. Attached logo for Verbica Partners has two variations - either can be used.

www.verbicapartners.com / www.kelvarho.com

```html
<!DOCTYPE html>
<html lang="en">
<head>
<meta charset="utf-8">
<title>Two-sided business card – Verbica Partners / Kelvarho</title>
<link rel="stylesheet" href="https://fonts.googleapis.com/css2?family=Arimo:wght@400;700&family=Crimson+Pro:wght@400;500;600&display=swap">
<style>
  :root {
    --stage-dark: #000000;
    --stage-light: #4d4d4d;
    --card-white: #ffffff;
    --band-green: #a2cd5a;
    --band-green-light: #c9e2a3;
    --mark-green: #7ab83d;
    --ink-navy: #2a2160;
    --ink-blue: #2b7cc0;
    --ink-white: #ffffff;
  }
  * { margin: 0; padding: 0; box-sizing: border-box; }
  html, body { width: 987px; height: 1200px; overflow: hidden; }
  body {
    position: relative;
    background: radial-gradient(ellipse 55% 45% at 50% 50%, var(--stage-light) 0%, #1c1c1c 60%, var(--stage-dark) 100%);
    font-family: "Arimo", Arial, sans-serif;
  }
  .card {
    position: absolute;
    left: 107px;
    width: 771px;
    height: 470px;
    background: var(--card-white);
    border-radius: 26px;
    overflow: hidden;
  }
  .card--verbica { top: 99px; }
  .card--kelvarho { top: 647px; }

  .brand {
    position: absolute;
    display: flex;
    align-items: center;
    gap: 12px;
  }
  .card--verbica .brand { left: 48px; top: 120px; }
  .brand__name--verbica {
    font-family: "Crimson Pro", Georgia, serif;
    font-weight: 500;
    font-size: 30px;
    letter-spacing: 2px;
    text-transform: uppercase;
    color: var(--ink-navy);
  }
  .card--kelvarho .brand { left: 46px; top: 58px; }
  .brand__dot {
    width: 50px; height: 50px;
    border-radius: 50%;
    background: var(--mark-green);
  }
  .brand__name--kelvarho {
    font-family: "Arimo", Arial, sans-serif;
    font-weight: 700;
    font-size: 58px;
    line-height: 1;
    color: var(--ink-blue);
  }

  .band {
    position: absolute;
    left: 0; width: 100%;
    background: var(--band-green);
    overflow: hidden;
  }
  .card--verbica .band { top: 181px; height: 216px; }
  .card--kelvarho .band { top: 167px; height: 216px; }

  .contact {
    position: absolute;
    left: 43px; top: 22px;
    color: var(--ink-white);
    line-height: 1.2;
  }
  .contact__name { font-size: 25px; font-weight: 400; -webkit-text-stroke: 0.4px var(--ink-white); }
  .contact__position { font-size: 24px; margin-bottom: 6px; }
  .contact__line { font-size: 21.5px; line-height: 27px; display: flex; align-items: center; gap: 8px; }
  .contact__line svg { width: 20px; height: 18px; flex: none; }

  .band__motif {
    position: absolute;
    right: 0;
    background: linear-gradient(135deg, var(--band-green) 0%, var(--band-green-light) 100%);
  }
  .card--verbica .band__motif { top: 6px; width: 211px; height: 152px; }
  .card--kelvarho .band__motif {
    top: 10px; width: 217px; height: 196px;
    background: linear-gradient(135deg, var(--band-green-light) 0%, #f2f8e8 100%);
  }

  .tagline {
    position: absolute;
    left: 43px;
    font-family: "Crimson Pro", Georgia, serif;
    font-weight: 500;
    font-size: 23.5px;
  }
  .card--verbica .tagline { top: 413px; color: var(--ink-navy); }
  .card--kelvarho .tagline { top: 413px; color: var(--ink-blue); }
</style>
</head>
<body>

<section class="card card--verbica" aria-label="Verbica Partners side">
  <div class="brand">
    <span class="brand__name brand__name--verbica">Verbica Partners</span>
  </div>
  <div class="band">
    <div class="contact">
      <p class="contact__name">Name</p>
      <p class="contact__position">Position</p>
      <p class="contact__line">
        <svg viewBox="0 0 20 18" aria-hidden="true"><path fill="#fff" d="M2 6c0-3 3-4 8-4s8 1 8 4v1h-4V5.5c-1-.6-2.5-.8-4-.8s-3 .2-4 .8V7H2zM5 8h10l3 8H2z"/><circle cx="10" cy="12" r="2" fill="#a2cd5a"/></svg>
        +61 3 5550 1427
      </p>
      <p class="contact__line">42 Tallis Lane</p>
      <p class="contact__line">Kewdale VIC 3190 Australia</p>
    </div>
    <div class="band__motif" role="img" aria-label="Large faint brand symbol decoration"></div>
  </div>
  <p class="tagline">Professional website translation and localisation that fits your budget</p>
</section>

<section class="card card--kelvarho" aria-label="Kelvarho side">
  <div class="brand">
    <span class="brand__dot" aria-hidden="true"></span>
    <span class="brand__name brand__name--kelvarho">Kelvarho</span>
  </div>
  <div class="band">
    <div class="contact">
      <p class="contact__name">Name</p>
      <p class="contact__position">Position</p>
      <p class="contact__line">
        <svg viewBox="0 0 20 18" aria-hidden="true"><path fill="#fff" d="M2 6c0-3 3-4 8-4s8 1 8 4v1h-4V5.5c-1-.6-2.5-.8-4-.8s-3 .2-4 .8V7H2zM5 8h10l3 8H2z"/><circle cx="10" cy="12" r="2" fill="#a2cd5a"/></svg>
        +61 3 5550 1427
      </p>
      <p class="contact__line">42 Tallis Lane</p>
      <p class="contact__line">Kewdale VIC 3190 Australia</p>
    </div>
    <div class="band__motif" role="img" aria-label="Large white brand symbol decoration"></div>
  </div>
  <p class="tagline">Professional website translation and localisation that fits your budget</p>
</section>

</body>
</html>
```